Design Some Double Sided Business Cards for a Printing Company

***WINNER WILL GET MORE BUSINESS CARD WORK AS A DIRECT HIRE***

Company is a print shop website that allows people to order printed materials such as business cards, brochures, banners, catalogs and more (like quorbelmart.com). The design should include elements for a print shop.

These business cards will incorporate Silver Foil (the grey part of logo will be silver foil for sure) and also Spot UV.

*Logo is attached. One file has transparent background (PDF file) and the other has a white background (JPG file). Use which one works best with your design

*Silver Foil will be on only ONE SIDE, not both

*Spot UV will also only be on ONE SIDE, not both

Both Foil and Spot UV may be on the same side or on different sides depending on the design. Be sure to create the artwork with Foil and Spot UV in mind to increase the look of your design.

***HERE IS INFO TO USE IN YOUR DESIGN***
(Name) Dale Hune
(Title) Ambassador of Print
(Phone) 731.509.3647
(email) info@zolkprinting.com
(web) www.zolkprinting.com

*DO NOT include info inside of the ( ) above

**I need many business card designs each week and looking to build a team of designers to directly hire for this work. Winner will be added to the team. The graphic designer of other great designs will be added to the team also.

Thanks!

```html
<!DOCTYPE html>
<html lang="en">
<head>
<meta charset="utf-8">
<title>Zolk Printing — Business Card</title>
<link rel="stylesheet" href="https://fonts.googleapis.com/css2?family=Questrial&display=swap">
<style>
  :root {
    --sky: #00c3f7;
    --sky-deep: #1aa6dc;
    --ink: #000000;
    --paper: #ffffff;
    --brand-blue: #2f8fd8;
    --link-blue: #2a9df0;
    --slate: #3d3d45;
    --grey-light: #8a8a8a;
    --grey-dark: #4a4a4a;
    --alert-red: #e8262b;
    --icon-blue: #3aa6ec;
    --icon-rim: #1d6fb8;
    --icon-ink: #0e2f4f;
  }
  * { margin: 0; padding: 0; box-sizing: border-box; }
  html, body {
    width: 1200px; height: 1200px; overflow: hidden;
    background: var(--paper);
    font-family: "Questrial", "Century Gothic", sans-serif;
  }
  .canvas { position: relative; width: 1200px; height: 1200px; }
  .card { position: absolute; left: 180px; width: 825px; height: 472px; overflow: hidden; }
  .card--front { top: 85px; background: var(--sky); }
  .card--back { top: 631px; background: var(--paper); }
  .card svg.shapes { position: absolute; inset: 0; }

  .world-map {
    position: absolute; left: 0; top: 0; width: 825px; height: 374px;
    background: radial-gradient(ellipse at 50% 45%, var(--sky-deep) 0%, var(--sky) 70%);
    opacity: 0.55;
  }

  .brand-box {
    position: absolute; display: flex; align-items: center; justify-content: center;
    background: var(--paper); border: 4px solid var(--brand-blue);
    color: var(--slate); white-space: nowrap; overflow: hidden;
    line-height: 1;
  }
  .brand-box .brand-square { background: var(--brand-blue); flex: none; }
  .card--front .brand-box { left: 215px; top: 83px; width: 394px; height: 107px; gap: 16px; padding: 0 20px; font-size: 36px; }
  .card--front .brand-square { width: 48px; height: 48px; }
  .card--back .brand-box { left: 283px; top: 13px; width: 260px; height: 69px; gap: 10px; padding: 0 12px; font-size: 23px; }
  .card--back .brand-square { width: 30px; height: 30px; }

  .front-url {
    position: absolute; left: 0; width: 825px; top: 392px;
    text-align: center; color: var(--link-blue); font-size: 42px; line-height: 50px;
  }

  .contact-line {
    position: absolute; color: #111; font-size: 31px; line-height: 38px; text-align: right; white-space: nowrap;
  }
  .contact-line--phone { right: 211px; top: 170px; }
  .contact-line--email { right: 239px; top: 250px; }
  .contact-line--web { right: 267px; top: 327px; }

  .back-url {
    position: absolute; left: 0; width: 825px; top: 432px;
    text-align: center; color: var(--alert-red); font-size: 33px; line-height: 40px;
  }
</style>
</head>
<body>
<main class="canvas">

  <section class="card card--front">
    <div class="world-map" role="img" aria-label="World map silhouette in a deeper blue across the card face"></div>
    <svg class="shapes" width="825" height="472" viewBox="0 0 825 472">
      <path d="M0 374 H353 L387 326 Q393 320 400 320 H413 Q420 320 426 326 L460 374 H825 V472 H0 Z" fill="var(--ink)"/>
      <line x1="0" y1="419" x2="192" y2="419" stroke="var(--link-blue)" stroke-width="2"/>
      <line x1="633" y1="419" x2="825" y2="419" stroke="var(--link-blue)" stroke-width="2"/>
    </svg>
    <div class="brand-box"><span class="brand-square"></span><span class="brand-name">ZOLK PRINTING</span></div>
    <p class="front-url">www.zolkprinting.com</p>
  </section>

  <section class="card card--back">
    <svg class="shapes" width="825" height="472" viewBox="0 0 825 472">
      <polygon points="0,92 140,92 80,433 0,433" fill="var(--grey-light)"/>
      <polygon points="647,92 825,92 825,433 547,433" fill="var(--grey-dark)"/>
      <path d="M0 0 H825 V92 H480 L446 136 Q440 142 433 142 H420 Q413 142 407 136 L373 92 H0 Z" fill="var(--ink)"/>
      <rect x="0" y="433" width="825" height="39" fill="var(--sky)"/>
      <g class="icon-phone" transform="translate(656 189)">
        <circle r="32" fill="var(--icon-rim)"/><circle r="27" fill="var(--icon-blue)"/>
        <rect x="-12" y="-17" width="24" height="34" rx="4" fill="var(--icon-ink)"/>
        <path d="M-5 -11 q-4 11 3 22 l4 -3 q-3 -4 -1 -8 l-1 -5 z" fill="var(--paper)"/>
      </g>
      <g class="icon-email" transform="translate(631 270)">
        <circle r="32" fill="var(--icon-rim)"/><circle r="27" fill="var(--icon-blue)"/>
        <rect x="-18" y="-12" width="36" height="24" fill="none" stroke="var(--icon-ink)" stroke-width="2.5"/>
        <polyline points="-18,-12 0,3 18,-12" fill="none" stroke="var(--icon-ink)" stroke-width="2.5"/>
        <line x1="-18" y1="12" x2="-5" y2="-1" stroke="var(--icon-ink)" stroke-width="2"/>
        <line x1="18" y1="12" x2="5" y2="-1" stroke="var(--icon-ink)" stroke-width="2"/>
      </g>
      <g class="icon-web" transform="translate(612 346)" fill="none" stroke="var(--icon-ink)" stroke-width="2.2">
        <circle r="32" fill="var(--icon-rim)" stroke="none"/><circle r="27" fill="var(--icon-blue)" stroke="none"/>
        <circle r="18"/><ellipse rx="8" ry="18"/>
        <line x1="-18" y1="0" x2="18" y2="0"/><line x1="0" y1="-18" x2="0" y2="18"/>
        <path d="M-15 -9 H15 M-15 9 H15"/>
      </g>
    </svg>
    <div class="brand-box"><span class="brand-square"></span><span class="brand-name">ZOLK PRINTING</span></div>
    <p class="contact-line contact-line--phone">731.509.3647</p>
    <p class="contact-line contact-line--email">info@zolkprinting.com</p>
    <p class="contact-line contact-line--web">www.zolkprinting.com</p>
    <p class="back-url">www.zolkprinting.com</p>
  </section>

</main>
</body>
</html>
```